Corporate Business Card

Very professional, Modern, Not to busy, include phone address email, website
(253) 555-0174, 61807 19th Street N, Kent, WA 98517, marcus@kestrelbayholding.com, brelvanindustries.com

Target Market(s)

Manufacturing

Industry/Entity Type

Aero, machining, manufacturing, Off road racing

Contact Information for Business Card

Phone, address email, website

```html
<!DOCTYPE html>
<html lang="en">
<head>
<meta charset="utf-8">
<title>Brelvan Industries – Business Card</title>
<link rel="stylesheet" href="https://fonts.googleapis.com/css2?family=Exo+2:wght@600;700&family=Roboto:wght@400&display=swap">
<style>
  :root {
    --backdrop: #333335;
    --navy: #2b3668;
    --navy-deep: #222c58;
    --red: #bd2127;
    --red-deep: #a81c22;
    --silver: #9c9c9f;
    --white: #ffffff;
    --ink-light: #f4e9e9;
  }
  html, body {
    margin: 0;
    padding: 0;
    width: 1200px;
    height: 1138px;
    overflow: hidden;
    background: var(--backdrop);
  }
  .canvas {
    position: relative;
    width: 1200px;
    height: 1138px;
  }
  .card {
    position: absolute;
    border-radius: 16px;
    overflow: hidden;
    background: var(--navy);
  }
  .card-back {
    left: 274px;
    top: 186px;
    width: 623px;
    height: 376px;
  }
  .card-front {
    left: 276px;
    top: 608px;
    width: 618px;
    height: 374px;
  }
  .pattern-field {
    position: absolute;
    inset: 0;
    background: linear-gradient(135deg, var(--navy-deep) 0%, var(--navy) 55%, #33407a 100%);
  }
  .wordmark {
    position: absolute;
    display: flex;
    align-items: center;
    gap: 10px;
    font-family: "Exo 2", sans-serif;
    font-weight: 700;
    color: var(--white);
    white-space: nowrap;
  }
  .wordmark-dot {
    width: 12px;
    height: 12px;
    background: var(--red);
  }
  .card-back .wordmark {
    left: 54px;
    top: 300px;
    font-size: 27px;
  }
  .card-front .wordmark {
    left: 52px;
    top: 92px;
    font-size: 31px;
  }
  .wave {
    position: absolute;
    inset: 0;
    width: 100%;
    height: 100%;
  }
  .holder-name {
    position: absolute;
    right: 27px;
    top: 198px;
    margin: 0;
    font-family: "Exo 2", sans-serif;
    font-weight: 700;
    font-size: 25px;
    letter-spacing: 0.5px;
    color: var(--white);
  }
  .contact-list {
    position: absolute;
    right: 27px;
    top: 246px;
    margin: 0;
    padding: 0;
    list-style: none;
    font-family: "Roboto", sans-serif;
    font-size: 16.5px;
    color: var(--ink-light);
    text-align: right;
  }
  .contact-list li {
    display: flex;
    justify-content: flex-end;
    align-items: center;
    gap: 12px;
    height: 24px;
  }
  .contact-list .address {
    margin-top: 4px;
  }
  .contact-icon {
    width: 14px;
    height: 14px;
    flex: none;
  }
</style>
</head>
<body>
<div class="canvas">

  <section class="card card-back">
    <div class="pattern-field" role="img" aria-label="Repeating tone-on-tone company mark pattern in deep navy"></div>
    <div class="wordmark"><span class="wordmark-dot"></span>Brelvan Industries</div>
  </section>

  <section class="card card-front">
    <svg class="wave" viewBox="0 0 618 374" preserveAspectRatio="none" aria-hidden="true">
      <defs>
        <linearGradient id="redFill" x1="0" y1="0" x2="0" y2="1">
          <stop offset="0" stop-color="#c4232a"/>
          <stop offset="1" stop-color="#a81c22"/>
        </linearGradient>
      </defs>
      <path d="M0,222 C140,290 300,255 400,175 C480,110 550,98 618,110" fill="none" stroke="#9c9c9f" stroke-width="10"/>
      <path d="M0,252 C160,295 310,255 420,185 C490,140 550,118 618,124 L618,374 L0,374 Z" fill="url(#redFill)"/>
    </svg>

    <div class="wordmark"><span class="wordmark-dot"></span>Brelvan Industries</div>

    <h1 class="holder-name">MARCUS HALE</h1>

    <ul class="contact-list">
      <li>(253) 555-0174
        <svg class="contact-icon" viewBox="0 0 16 16" aria-hidden="true"><path fill="#f4e9e9" d="M3.6 1.5l2.3 2.3-1.3 1.9c.9 2.1 2.6 3.8 4.7 4.7l1.9-1.3 2.3 2.3-1.6 2.4C7.3 14.1 1.9 8.7 1.2 3.1z"/></svg>
      </li>
      <li>www.brelvanindustries.com
        <svg class="contact-icon" viewBox="0 0 16 16" aria-hidden="true"><circle cx="8" cy="8" r="6.5" fill="none" stroke="#f4e9e9" stroke-width="1.4"/><path d="M1.5 8h13M8 1.5c-3 3.5-3 9.5 0 13M8 1.5c3 3.5 3 9.5 0 13" fill="none" stroke="#f4e9e9" stroke-width="1.2"/></svg>
      </li>
      <li>marcus@kestrelbayholding.com
        <svg class="contact-icon" viewBox="0 0 16 16" aria-hidden="true"><rect x="1" y="3" width="14" height="10" fill="none" stroke="#f4e9e9" stroke-width="1.4"/><path d="M1 3l7 6 7-6" fill="none" stroke="#f4e9e9" stroke-width="1.4"/></svg>
      </li>
      <li class="address">61807 19th Street N, Kent, WA 98517</li>
    </ul>
  </section>

</div>
</body>
</html>
```